New tech executive consulting company needs professionally branded document templates

We are a new business selling fractional board advisory and go-to-market consulting services into the Technology space. Partwise Helm are experts in providing high-quality executive-level leaders on a part-time basis to tech companies in need of their expertise. We work closely with clients to understand their business needs, challenges, and goals, and provides customised solutions to help them succeed. Due to our audience we need the design to have a high quality, executive look and feel.

Our first website is live and can be found at partwisehelm.tech. We also already have a logo which I've uploaded. Our brand is clean and uses orange to give it colour and an identity that stands out.

We need some document master templates created so we can create our own presentations (Google Slides & Powerpoint), PDF documents, and Word templates, and ideally also a LinkedIn banner.

```html
<!DOCTYPE html>
<html lang="en">
<head>
<meta charset="utf-8">
<title>Partwise Helm – Presentation Master Templates</title>
<link rel="stylesheet" href="https://fonts.googleapis.com/css2?family=Outfit:wght@300;400;500;600&family=Playfair+Display:wght@600;700&display=swap">
<style>
  :root{
    --board:#bfc2c6;
    --navy:#272f3e;
    --orange:#ec844b;
    --white:#ffffff;
    --ink:#2b3240;
    --photo-warm:#8f8a80;
    --photo-cool:#5d6d7a;
  }
  *{margin:0;padding:0;box-sizing:border-box}
  html,body{width:1200px;height:714px;overflow:hidden;background:var(--board)}
  .board{position:relative;width:1200px;height:714px;overflow:hidden;background:var(--board);font-family:"Outfit",sans-serif;color:var(--ink)}
  .slide{position:absolute;width:760px;height:428px;overflow:hidden;background:var(--white);transform:scale(0.4816);transform-origin:0 0}
  .slide svg.bg{position:absolute;inset:0;width:760px;height:428px}
  .col-1{left:34px}.col-2{left:417px}.col-3{left:800px}
  .row-1{top:31px}.row-2{top:254px}.row-3{top:477px}
  .dark{background:var(--navy);color:var(--white)}
  .abs{position:absolute}
  .brand{font-family:"Outfit",sans-serif;font-weight:600;font-size:24px;letter-spacing:1.5px;color:var(--navy);line-height:1}
  .title-xl{font-family:"Playfair Display",serif;font-weight:700;font-size:36px;line-height:1.1;color:var(--navy)}
  .title-l{font-family:"Playfair Display",serif;font-weight:700;font-size:30px;line-height:1.18}
  .on-dark{color:var(--white)}
  .subhead{font-size:17px;font-weight:400;color:var(--navy)}
  .body{font-size:10px;font-weight:300;line-height:1.5}
  .eyebrow{font-size:11px;color:var(--orange);letter-spacing:.3px}
  .url{font-size:10px;color:var(--white)}
  .page-no{position:absolute;right:12px;bottom:12px;font-size:6px}
  .stat-value{font-family:"Playfair Display",serif;font-weight:600;font-size:52px;color:var(--orange);line-height:1}
  .label{font-size:16px;font-weight:400;color:var(--navy)}
  .quote-mark{font-family:"Playfair Display",serif;font-weight:700;font-size:130px;line-height:1;color:var(--white)}
  .quote-text{font-size:13px;line-height:1.45;color:var(--white);text-align:center}
</style>
</head>
<body>
<main class="board">

  <!-- Cover -->
  <section class="slide col-1 row-1">
    <svg class="bg" viewBox="0 0 760 428">
      <defs><linearGradient id="g-office" x1="0" y1="0" x2="1" y2="1"><stop offset="0" stop-color="#c9d3d6"/><stop offset=".5" stop-color="#8f8a80"/><stop offset="1" stop-color="#4d535a"/></linearGradient></defs>
      <rect x="0" y="363" width="760" height="65" fill="var(--navy)"/>
      <polygon points="545,0 760,0 760,428 262,428" fill="url(#g-office)" role="img" aria-label="Photo: team meeting in a bright office"/>
      <polygon points="489,0 545,0 262,428 209,428" fill="var(--orange)"/>
    </svg>
    <div class="abs brand" style="left:36px;top:50px">PARTWISE HELM</div>
    <h1 class="abs title-xl" style="left:36px;top:150px">Head Title</h1>
    <p class="abs subhead" style="left:36px;top:198px">Subhead Title</p>
    <p class="abs body" style="left:36px;top:230px;width:220px">Lorem ipsum dolor sit amet, consectetuer adipiscing elit, sed diam nonum</p>
    <p class="abs url" style="left:38px;top:381px">partwisehelm.tech</p>
  </section>

  <!-- About -->
  <section class="slide dark col-2 row-1">
    <svg class="bg" viewBox="0 0 760 428">
      <defs><linearGradient id="g-pair" x1="0" y1="0" x2="1" y2="1"><stop offset="0" stop-color="#e9e6e1"/><stop offset=".6" stop-color="#9a9590"/><stop offset="1" stop-color="#3f4a5c"/></linearGradient></defs>
      <polygon points="589,35 725,35 725,392 359,392" fill="url(#g-pair)" role="img" aria-label="Photo: two colleagues reviewing a tablet"/>
      <polygon points="555,0 612,0 335,428 278,428" fill="var(--orange)"/>
      <line x1="712" y1="428" x2="760" y2="355" stroke="var(--orange)" stroke-width="3"/>
    </svg>
    <p class="abs eyebrow" style="left:36px;top:53px">ABOUT</p>
    <h2 class="abs title-l on-dark" style="left:36px;top:75px">The smart way to<br>scale your business</h2>
    <div class="abs body" style="left:36px;top:163px;width:270px">
      <p>Partwise Helm are experts in providing high-quality executive-level leaders on a part-time basis to tech companies in need of their expertise. We work closely with clients to understand their business needs, challenges, and goals, and provides customised solutions to help them succeed.</p>
      <p style="margin-top:15px">Our strategic insights, leadership, and collaborative approach make us a valuable partner for companies looking to drive growth and innovation. We are passionate about helping companies achieve their goals and are committed to providing the highest level of service to our clients.</p>
    </div>
    <span class="page-no">1</span>
  </section>

  <!-- Profile -->
  <section class="slide col-3 row-1">
    <svg class="bg" viewBox="0 0 760 428">
      <defs><linearGradient id="g-portrait" x1="0" y1="0" x2="1" y2="1"><stop offset="0" stop-color="#5a6a55"/><stop offset=".5" stop-color="#b08b72"/><stop offset="1" stop-color="#2c3f66"/></linearGradient></defs>
      <rect x="0" y="0" width="760" height="156" fill="var(--navy)"/>
      <rect x="36" y="35" width="317" height="357" fill="url(#g-portrait)" role="img" aria-label="Portrait photo of the founder"/>
      <polygon points="83,0 112,0 0,172 0,127" fill="var(--orange)"/>
      <line x1="712" y1="428" x2="760" y2="355" stroke="var(--orange)" stroke-width="3"/>
    </svg>
    <h2 class="abs title-l on-dark" style="left:404px;top:102px">BEN HARLOW</h2>
    <div class="abs body" style="left:404px;top:175px;width:320px">
      <p>Ben Harlow is a highly accomplished business leader with extensive experience in executive-level leadership and strategy. As the founder of Partwise Helm, Ben brings his years of experience in the technology industry to help companies achieve their goals.</p>
      <p style="margin-top:12px">Throughout his career, Ben has held executive positions in companies ranging from startups to large corporations. He has a deep understanding of the tech industry and has helped companies at all stages of maturity drive significant growth and innovation.</p>
    </div>
    <span class="page-no">2</span>
  </section>

  <!-- Stats -->
  <section class="slide col-1 row-2">
    <svg class="bg" viewBox="0 0 760 428">
      <rect x="0" y="0" width="760" height="120" fill="var(--navy)"/>
      <line x1="712" y1="428" x2="760" y2="355" stroke="var(--orange)" stroke-width="3"/>
    </svg>
    <h2 class="abs title-l on-dark" style="left:36px;top:60px">Heading Title</h2>
    <div class="abs" style="left:36px;top:170px;width:190px">
      <p class="stat-value">30%</p><p class="label" style="margin-top:18px">Lorem ipsum</p>
      <p class="body" style="margin-top:8px">Lorem ipsum dolor sit amet, consectetuer adipiscing elit, sed diam nonummy nibh euismod tincidunt ut laoreet dolore magna aliquam erat volutpat. Ut wisi enim ad minim</p>
    </div>
    <div class="abs" style="left:292px;top:170px;width:190px">
      <p class="stat-value">40%</p><p class="label" style="margin-top:18px">Lorem ipsum</p>
      <p class="body" style="margin-top:8px">Lorem ipsum dolor sit amet, consectetuer adipiscing elit, sed diam nonummy nibh euismod tincidunt ut laoreet dolore magna aliquam erat volutpat. Ut wisi enim ad minim</p>
    </div>
    <div class="abs" style="left:549px;top:170px;width:190px">
      <p class="stat-value">30%</p><p class="label" style="margin-top:18px">Lorem ipsum</p>
      <p class="body" style="margin-top:8px">Lorem ipsum dolor sit amet, consectetuer adipiscing elit, sed diam nonummy nibh euismod tincidunt ut laoreet dolore magna aliquam erat volutpat. Ut wisi enim ad minim</p>
    </div>
    <span class="page-no">3</span>
  </section>

  <!-- Image + text -->
  <section class="slide col-2 row-2">
    <svg class="bg" viewBox="0 0 760 428">
      <defs><linearGradient id="g-team" x1="0" y1="0" x2="1" y2="1"><stop offset="0" stop-color="#7b6a5e"/><stop offset=".5" stop-color="#4c5563"/><stop offset="1" stop-color="#a18c7c"/></linearGradient></defs>
      <rect x="0" y="0" width="760" height="233" fill="var(--navy)"/>
      <polygon points="0,0 725,0 585,233 0,233" fill="url(#g-team)" role="img" aria-label="Photo: team gathered around a boardroom table"/>
      <polygon points="725,0 760,0 760,8 610,248 565,248" fill="var(--orange)"/>
      <line x1="712" y1="428" x2="760" y2="355" stroke="var(--orange)" stroke-width="3"/>
    </svg>
    <h2 class="abs title-l" style="left:36px;top:270px;color:var(--navy)">Heading Title</h2>
    <div class="abs body" style="left:288px;top:270px;width:440px">
      <p>Lorem ipsum dolor sit amet, consectetuer adipiscing elit, sed diam nonummy nibh euismod tincidunt ut laoreet dolore magna aliquam erat volutpat. Ut wisi enim ad minim Lorem ipsum dolor sit amet, consectetuer adipiscing elit, sed diam nonummy nibh euismod tincidunt ut laoreet dolore magna aliquam erat volutpat. Ut wisi enim ad minim</p>
      <p style="margin-top:15px">sed diam nonummy nibh euismod tincidunt ut laoreet dolore magna aliquam erat volutpat. Ut wisi enim ad minim.</p>
    </div>
    <span class="page-no">4</span>
  </section>

  <!-- Quote -->
  <section class="slide col-3 row-2">
    <svg class="bg" viewBox="0 0 760 428">
      <defs><linearGradient id="g-desk" x1="0" y1="0" x2="1" y2="1"><stop offset="0" stop-color="#2c3544"/><stop offset=".5" stop-color="#3e4858"/><stop offset="1" stop-color="#565f6c"/></linearGradient></defs>
      <rect x="0" y="0" width="760" height="428" fill="url(#g-desk)" role="img" aria-label="Dimmed photo: hands working at a desk with a laptop"/>
      <line x1="712" y1="428" x2="760" y2="355" stroke="var(--orange)" stroke-width="3"/>
    </svg>
    <p class="abs quote-mark" style="left:0;width:760px;text-align:center;top:108px">“</p>
    <p class="abs quote-text" style="left:180px;width:400px;top:208px">Lorem ipsum dolor sit amet, consectetuer adipiscing elit, sed diam nonummy nibh euismod tincidunt ut laoreet dolore magna aliquam erat volutpat.</p>
    <p class="abs eyebrow" style="left:0;width:760px;text-align:center;top:295px">YOUR NAME</p>
    <span class="page-no" style="color:var(--white)">5</span>
  </section>

  <!-- Timeline -->
  <section class="slide col-1 row-3">
    <svg class="bg" viewBox="0 0 760 428">
      <rect x="0" y="0" width="760" height="120" fill="var(--navy)"/>
      <line x1="36" y1="257" x2="725" y2="257" stroke="var(--orange)" stroke-width="1"/>
      <g fill="var(--orange)"><circle cx="36" cy="257" r="3.5"/><circle cx="176" cy="257" r="3.5"/><circle cx="316" cy="257" r="3.5"/><circle cx="456" cy="257" r="3.5"/><circle cx="596" cy="257" r="3.5"/></g>
      <line x1="712" y1="428" x2="760" y2="355" stroke="var(--orange)" stroke-width="3"/>
    </svg>
    <h2 class="abs title-l on-dark" style="left:36px;top:60px">Heading Title</h2>
    <div class="abs" style="left:176px;top:192px;width:130px"><p class="label" style="font-size:14px">Lorem ipsum</p><p class="body" style="font-size:8.5px;margin-top:4px">Lorem ipsum dolor sit amet, consectetuer adipiscing elit.</p></div>
    <div class="abs" style="left:456px;top:192px;width:130px"><p class="label" style="font-size:14px">Lorem ipsum</p><p class="body" style="font-size:8.5px;margin-top:4px">Lorem ipsum dolor sit amet, consectetuer adipiscing elit.</p></div>
    <div class="abs" style="left:36px;top:265px;width:130px"><p class="label" style="font-size:14px">Lorem ipsum</p><p class="body" style="font-size:8.5px;margin-top:4px">Lorem ipsum dolor sit amet, consectetuer adipiscing elit.</p></div>
    <div class="abs" style="left:316px;top:265px;width:130px"><p class="label" style="font-size:14px">Lorem ipsum</p><p class="body" style="font-size:8.5px;margin-top:4px">Lorem ipsum dolor sit amet, consectetuer adipiscing elit.</p></div>
    <div class="abs" style="left:596px;top:265px;width:130px"><p class="label" style="font-size:14px">Lorem ipsum</p><p class="body" style="font-size:8.5px;margin-top:4px">Lorem ipsum dolor sit amet, consectetuer adipiscing elit.</p></div>
  </section>

  <!-- Split text -->
  <section class="slide col-2 row-3">
    <svg class="bg" viewBox="0 0 760 428">
      <polygon points="0,0 345,0 68,428 0,428" fill="var(--navy)"/>
      <polygon points="345,0 400,0 123,428 68,428" fill="var(--orange)"/>
      <line x1="712" y1="428" x2="760" y2="355" stroke="var(--orange)" stroke-width="3"/>
    </svg>
    <h2 class="abs title-l on-dark" style="left:36px;top:60px">Heading<br>Title</h2>
    <div class="abs body" style="left:351px;top:153px;width:370px">
      <p>Lorem ipsum dolor sit amet, consectetuer adipiscing elit, sed diam nonummy nibh euismod tincidunt ut laoreet dolore magna aliquam erat volutpat. Ut wisi enim ad minim Lorem ipsum dolor sit amet, consectetuer adipiscing elit, sed diam nonummy nibh euismod tincidunt ut laoreet dolore magna aliquam erat volutpat. Ut wisi enim ad minim</p>
      <p style="margin-top:15px">sed diam nonummy nibh euismod tincidunt ut laoreet dolore magna aliquam erat volutpat. Ut wisi enim ad minim.</p>
    </div>
    <span class="page-no">7</span>
  </section>

  <!-- Closing -->
  <section class="slide col-3 row-3">
    <svg class="bg" viewBox="0 0 760 428">
      <defs><linearGradient id="g-office2" x1="0" y1="0" x2="1" y2="1"><stop offset="0" stop-color="#c9d3d6"/><stop offset=".5" stop-color="#8f8a80"/><stop offset="1" stop-color="#4d535a"/></linearGradient></defs>
      <rect x="0" y="363" width="760" height="65" fill="var(--navy)"/>
      <polygon points="545,0 760,0 760,428 262,428" fill="url(#g-office2)" role="img" aria-label="Photo: team meeting in a bright office"/>
      <polygon points="489,0 545,0 262,428 209,428" fill="var(--orange)"/>
    </svg>
    <div class="abs brand" style="left:36px;top:50px">PARTWISE HELM</div>
    <h2 class="abs title-xl" style="left:36px;top:190px">Thank You</h2>
    <p class="abs url" style="left:38px;top:381px">partwisehelm.tech</p>
  </section>

</main>
</body>
</html>
```